Travinex - You are the Boss!

Travinex is a new Silicon Valley company, of the pelim founders from Berlin, which provides a "Shared Pioneer Circle". This platform allows the crowd to support startups with money, experts and fame. Our Vision is, that everyone should become an entrepreneur.

Pls find all brief details in the attached document
Updates

Would be nice to have a list of more social services I'm available on, like a list of pictograms of all my services:

Find me on: vooka, bramlet+, qrt, fenwix, moodrail, zupp, hvoxa, etc...

pls make sure to use the right font:
http://www.typemarlow.com/fonts/Velquin

Target Market(s)

Main target market is those already involved in the startup industry, by fundraising, investing, advising, cofounding and working. Travinex brings a totaly new transparency and collaborative way of starting companies to that business.

· Entrepreneurs (looking for funding, team and community)
· Investors (looking for hot investments and )
· Experts (workers looking for startups they can work for equity)
· Incubators & Business Schools (looking for tools to advise startups)

Industry/Entity Type

It Company

Requirements
Must have
• Pls find all brief details in the attached document
Nice to have

```html
<!DOCTYPE html>
<html lang="en">
<head>
<meta charset="utf-8">
<title>Travinex – Business Card</title>
<link href="https://fonts.googleapis.com/css2?family=Arimo:wght@400;700&display=swap" rel="stylesheet">
<style>
  :root {
    --page: #ffffff;
    --card-light: #e4e5e5;
    --card-mid: #c9cbcb;
    --card-dark: #b4b6b6;
    --ink: #1c1c1c;
    --ink-soft: #3a3a3a;
    --accent: #3fd0e2;
    --ghost: rgba(255,255,255,0.3);
  }
  html, body { margin: 0; padding: 0; overflow: hidden; }
  body { width: 1200px; height: 363px; background: var(--page); position: relative; font-family: "Arimo", Arial, sans-serif; }
  .card {
    position: absolute; top: 11px; height: 341px; overflow: hidden;
    background: radial-gradient(ellipse at 50% 45%, var(--card-light) 0%, var(--card-mid) 55%, var(--card-dark) 100%);
  }
  .card--front { left: 11px; width: 585px; }
  .card--back { left: 607px; width: 584px; }
  .pattern { position: absolute; inset: 0;
    background: linear-gradient(180deg, rgba(255,255,255,0.12), rgba(255,255,255,0) 60%, rgba(0,0,0,0.05)); }
  .ghost-name {
    position: absolute; font-family: "Arimo", Arial, sans-serif; font-weight: 700;
    color: var(--ghost); font-size: 78px; white-space: nowrap; line-height: 1;
  }
  .bar { position: absolute; background: var(--accent); }
  .notch { position: absolute; background: var(--page); }
  .wordmark {
    position: absolute; font-family: "Arimo", Arial, sans-serif; font-weight: 700;
    color: var(--ink); white-space: nowrap; line-height: 1; margin: 0;
  }
  .logo-symbol {
    position: absolute; border-radius: 50%;
    background: radial-gradient(ellipse at 50% 40%, #3a3a3a 0%, #1c1c1c 70%);
  }
  .tagline {
    position: absolute; font-family: "Arimo", Arial, sans-serif; font-weight: 700;
    color: var(--ink-soft); white-space: nowrap; line-height: 1; margin: 0;
  }
  .person-name { position: absolute; left: 34px; top: 140px; margin: 0; font-size: 21px; font-weight: 700; color: var(--accent); line-height: 1; }
  .person-role { position: absolute; left: 80px; top: 164px; margin: 0; font-size: 12px; color: var(--ink-soft); line-height: 1; }
  .contacts { position: absolute; top: 181px; margin: 0; padding: 0; list-style: none; }
  .contacts--a { left: 118px; }
  .contacts--b { left: 301px; }
  .contacts li { height: 19px; display: flex; align-items: center; font-size: 12.5px; color: var(--ink-soft); white-space: nowrap; }
  .icon { width: 13px; height: 13px; margin-right: 9px; flex: none; display: block; }
  .dot { width: 11px; height: 11px; margin: 0 10px 0 1px; border-radius: 50%; background: var(--ink); flex: none; }
  .web { position: absolute; left: 0; right: 0; top: 285px; text-align: center; margin: 0; color: var(--accent); font-size: 12px; letter-spacing: 6px; }
</style>
</head>
<body>

<section class="card card--front">
  <div class="pattern" role="img" aria-label="Faint pixel-game creature pattern in light grey"></div>
  <span class="ghost-name" style="left:20px; top:98px;">travinex</span>
  <div class="bar" style="left:222px; top:0; width:351px; height:20px;"></div>
  <div class="notch" style="left:529px; top:20px; width:44px; height:22px;"></div>
  <div class="bar" style="left:0; top:238px; width:19px; height:92px;"></div>
  <div class="notch" style="left:19px; top:251px; width:18px; height:90px;"></div>
  <h1 class="wordmark" style="left:60px; top:92px; font-size:64px; letter-spacing:10px;">TRAVINEX</h1>
  <div class="logo-symbol" role="img" aria-label="Client logo symbol" style="left:70px; top:150px; width:200px; height:58px;"></div>
  <p class="tagline" style="left:302px; top:142px; font-size:15px;">YOU ARE THE BOSS!</p>
</section>

<section class="card card--back">
  <div class="pattern" role="img" aria-label="Faint pixel-game creature pattern in light grey"></div>
  <span class="ghost-name" style="left:40px; top:52px;">travinex</span>
  <div class="bar" style="left:0; top:0; width:351px; height:20px;"></div>
  <div class="notch" style="left:0; top:20px; width:45px; height:22px;"></div>
  <div class="bar" style="left:565px; top:241px; width:19px; height:89px;"></div>
  <div class="notch" style="left:547px; top:254px; width:18px; height:87px;"></div>
  <h2 class="wordmark" style="left:92px; top:58px; font-size:52px; letter-spacing:8px;">TRAVINEX</h2>
  <div class="logo-symbol" role="img" aria-label="Client logo symbol" style="left:198px; top:112px; width:110px; height:34px;"></div>
  <p class="tagline" style="left:302px; top:102px; font-size:13px;">YOU ARE THE BOSS!</p>

  <p class="person-name">Lorin Feltz</p>
  <p class="person-role">Founder and CTO</p>

  <ul class="contacts contacts--a">
    <li><svg class="icon" viewBox="0 0 13 13"><rect x="0.5" y="2.5" width="12" height="8" fill="#1c1c1c"/><path d="M0.5 2.5 L6.5 7 L12.5 2.5" fill="none" stroke="#c9cbcb" stroke-width="1"/></svg>lfe@travinex.com</li>
    <li><svg class="icon" viewBox="0 0 13 13"><path d="M3 1 h3 l1 3 -1.5 1 a7 7 0 0 0 2.5 2.5 l1 -1.5 3 1 v3 a1 1 0 0 1 -1 1 A10 10 0 0 1 2 2 a1 1 0 0 1 1 -1z" fill="#1c1c1c"/></svg>000.000.0000</li>
    <li><span class="dot"></span>friendlane.com/lorinfeltz</li>
    <li><span class="dot"></span>bramlet+/lorinfeltz</li>
    <li><span class="dot"></span>fenwix/lorinfeltz</li>
  </ul>

  <ul class="contacts contacts--b">
    <li><span class="dot"></span>www.vooka.com/lorinfeltz</li>
    <li><span class="dot"></span>chirpa.com/lorin_feltz</li>
    <li><span class="dot"></span>linkrow.com/lorinfeltz</li>
    <li><span class="dot"></span>qrt/lorinfeltz</li>
    <li><span class="dot"></span>moodrail/lorinfeltz</li>
  </ul>

  <p class="web">WWW.TRAVINEX.COM</p>
</section>

</body>
</html>
```